Two Versions of a Business Card for a Lawyer

Summary: I need a logo and a business card. The business card is two-sided and comes in two versions. One version is conservative, the other is slightly different with one or more pink embellishments in the logo or somewhere else in the business card.
I'm about to start off as a sole practitioner in criminal and immigration law. I'll largely be working with marginalised communities and in areas of social justice. One of my main focuses will be gendered violence, I'm hoping to specialise my practice towards representing victims of domestic and sexual violence and sex workers. I want a business card which would attract this clientele and make them feel safe to speak with me. I'd also like it to communicate a sense of hope.
However, the business card still has to be very conservative as the legal profession is very stuffy. So I was thinking of having two versions of the same card, one would be very straight forward while the other would have a **pink embellishment** or perhaps several. For example, if the scales of justice were used in the design, maybe the second version would have a pink flower about to bloom on the scale somewhere. Or maybe it's my logo that is different and pink.
While both designs have to be pretty conservative, I still want it to give off a sense that I'm alternative and think outside the box. With lawyers, I think a little bit of deviation goes a long way (less is more).
As far as colour goes (other than the pink embellishment), I was thinking something monochromatic, probably black and white but I am open to considering more colours. I personally love colour, and would love to use more colour, but am hesitant because of the nature of the profession. If you can find a way to use more colour while keeping it conservative and letting the pink pop, I'd be pretty pleased.
In general, I would prefer a clean simplistic design and logo. It should be immediately obvious that I'm a lawyer just by glancing at the card. I'm open to symbols of law, like the scales of justice or lady justice or something else. However, I don't want it to be the same as everyone else's.
Eventually, the design/style should be easy to recreate in the form of a website.
As far as the logo goes, it would probably use a circle as my last name starts with the letter "O". It can be very simple, with just my name and "Barrister & Solicitor". I don't currently have a logo, but the winning designer will be invited to provide a separate file for just the logo for an additional fee (I think it was CA$99). (Please ignore the uploaded logo file, it just wouldn't let me continue without uploading something).
As for the information that should go into the card, I'm still finalizing my address and phone number. So please use a placeholder for now.
Target Market(s)
Women, victims of sexual or domestic violence, refugees, people in need of legal services
Industry/Entity Type
Lawyer
Contact Information for Business Card
Maren Vickery
Barrister & Solicitor
LL.B., B.C.L., B.F.A.
Criminal & Immigration Law
Street address
Toronto, ON
Postal Code
Phone number
Fax number
Email
Logo Text
Maren Vickery, Barrister & Solicitor
Requirements
Must have
- Two versions
- One with pink
- Simplistic
Nice to have
- Maybe more colour
Should not have
- Not too conservative
- Not too predictable

```html
<!DOCTYPE html>
<html lang="en">
<head>
<meta charset="utf-8">
<title>Maren Vickery — Barrister &amp; Solicitor</title>
<link rel="stylesheet" href="https://fonts.googleapis.com/css2?family=Crimson+Pro:ital,wght@1,600;1,700&display=swap">
<style>
  :root {
    --rose: #d0688a;
    --rose-deep: #c25a7d;
    --paper: #ffffff;
    --ink-light: #ffffff;
  }
  html, body {
    margin: 0;
    padding: 0;
    width: 686px;
    height: 1200px;
    overflow: hidden;
    background: var(--paper);
  }
  .card {
    position: relative;
    width: 686px;
    height: 1200px;
    background: var(--paper);
    font-family: "Crimson Pro", "Palatino Linotype", Georgia, serif;
    font-style: italic;
    overflow: hidden;
  }
  .card__band {
    position: absolute;
    left: 0;
    top: 0;
    width: 686px;
    height: 600px;
    background: var(--rose);
  }
  .card__rule {
    position: absolute;
    left: 0;
    top: 614px;
    width: 686px;
    height: 2px;
    background: var(--rose);
    opacity: 0.55;
  }
  .monogram {
    position: absolute;
    left: 34px;
    top: 268px;
    margin: 0;
    font-size: 360px;
    line-height: 1;
    font-weight: 700;
    color: var(--ink-light);
  }
  .name {
    position: absolute;
    left: 272px;
    margin: 0;
    font-size: 104px;
    line-height: 1;
    font-weight: 700;
    color: var(--ink-light);
  }
  .name--given { top: 340px; }
  .name--family { top: 466px; }
  .title {
    position: absolute;
    left: 40px;
    top: 632px;
    margin: 0;
    font-size: 35px;
    font-weight: 600;
    color: var(--rose-deep);
  }
  .ornament {
    position: absolute;
    right: 0;
    bottom: 0;
    width: 176px;
    height: 176px;
    background: linear-gradient(135deg, #f3d3de 0%, #d98aa6 100%);
  }
</style>
</head>
<body>
  <main class="card">
    <div class="card__band"></div>
    <div class="card__rule"></div>
    <h1 class="card__logo" aria-label="Maren Vickery">
      <span class="monogram" aria-hidden="true">V</span>
      <span class="name name--given" aria-hidden="true">Maren</span>
      <span class="name name--family" aria-hidden="true">ickery</span>
    </h1>
    <p class="title">Barrister &amp; Solicitor</p>
    <div class="ornament" role="img" aria-label="Decorative pink flourish ornament in the corner"></div>
  </main>
</body>
</html>
```